I need a business card design for my new clinic (SPORTS MEDICINE OF KNEE). I am orthopedist, expert in sports surgery, especially knee surgery. I prefer, as colors, the colors of my logo (green, black and white). I already have my logo and should appear on my card. It's good to see my site to have ideas (www.drlucianovarela.com)
It needs contain:
my name: Dr. Luciano Varela
my registration: CRM 584-902
my specialty: Cirurgia do Joelho / Esporte
my address: Centro Executivo - Pinheiral Plaza
Av. Doutor Augusto Brandão Cunha, 2740 sala 0836
Jd. Ipanema - Vila Serena - VS
my phone number: Tel (10) 8245-3908
my clinic phone: (10) 3670-4851
my e-mail: drlucianovarela@mailbox-exemplo.com
my site: www.drlucianovarela.com

Target Market(s)

futures patients

Industry/Entity Type

Clinic

Requirements
Nice to have
• letters not overfilled
straight lines, with few curves

```html
<!DOCTYPE html>
<html lang="pt-BR">
<head>
<meta charset="utf-8">
<title>Varela Traumatologia Esportiva – Cartão de Visita</title>
<link rel="stylesheet" href="https://fonts.googleapis.com/css2?family=Cinzel:wght@600&family=Crimson+Text&family=Open+Sans:ital,wght@0,400;0,700;1,400&display=swap">
<style>
  :root {
    --green: #4dc08b;
    --green-light: #6fd3a3;
    --green-dark: #34a873;
    --black: #111111;
    --white: #ffffff;
    --ink: #3a3a3a;
    --backdrop: #6e5438;
  }
  * { margin: 0; padding: 0; box-sizing: border-box; }
  html, body { width: 882px; height: 1200px; overflow: hidden; }
  body { background: var(--backdrop); position: relative; font-family: "Open Sans", sans-serif; }

  .card {
    position: absolute; left: 121px; width: 640px; height: 366px;
    border-radius: 6px; overflow: hidden;
    box-shadow: 0 14px 30px rgba(0,0,0,.35);
  }

  /* Front */
  .card-front {
    top: 72px;
    background: linear-gradient(135deg, var(--green-light), var(--green) 55%, var(--green-dark));
  }
  .front-brand { position: absolute; left: 48px; top: 110px; display: flex; align-items: center; gap: 26px; }
  .brand-square { width: 96px; height: 96px; border-radius: 12px; background: var(--black); flex: none; }
  .front-name { font-family: "Cinzel", serif; font-weight: 600; font-size: 92px; line-height: 1; color: var(--black); letter-spacing: 2px; }
  .front-tagline { font-family: "Crimson Text", serif; font-size: 30px; color: var(--white); margin-top: 4px; letter-spacing: 1px; }
  .front-band {
    position: absolute; left: 0; right: 0; bottom: 0; height: 48px; background: var(--black);
    display: flex; align-items: center; justify-content: flex-end; padding-right: 28px; gap: 10px;
  }
  .front-band .site { color: var(--white); font-size: 15px; letter-spacing: 2px; }
  .front-band .site b { color: var(--green); font-weight: 400; }

  /* Back */
  .card-back { top: 700px; background: var(--white); }
  .icon-tab {
    position: absolute; left: 0; top: 134px; width: 28px; height: 80px;
    background: var(--green); border-radius: 0 14px 14px 0;
    display: flex; flex-direction: column; justify-content: space-around; align-items: center; padding: 6px 0;
  }
  .back-content { position: absolute; left: 42px; top: 30px; }
  .doctor-name { font-weight: 700; font-style: italic; font-size: 24px; color: var(--black); }
  .specialty { font-style: italic; font-size: 15px; color: var(--green); margin-bottom: 14px; }
  .contact-line { font-size: 12.5px; color: var(--ink); line-height: 20px; }
  .back-brand { position: absolute; right: 34px; top: 200px; }
  .back-brand-row { display: flex; align-items: center; gap: 12px; }
  .back-brand .brand-square { width: 46px; height: 46px; border-radius: 7px; }
  .back-name { font-family: "Cinzel", serif; font-weight: 600; font-size: 46px; line-height: 1; color: var(--black); }
  .back-tagline { font-family: "Crimson Text", serif; font-size: 16px; color: var(--green); margin-left: 58px; }
  .registration { position: absolute; left: 42px; bottom: 26px; font-size: 14px; color: var(--ink); }
  .registration em { color: var(--green); }
</style>
</head>
<body>

<section class="card card-front" aria-label="Frente do cartão">
  <div class="front-brand">
    <span class="brand-square"></span>
    <div>
      <div class="front-name">VARELA</div>
      <div class="front-tagline">Traumatologia Esportiva</div>
    </div>
  </div>
  <div class="front-band">
    <svg width="16" height="16" viewBox="0 0 16 16" aria-hidden="true">
      <circle cx="8" cy="8" r="7" fill="none" stroke="#4dc08b" stroke-width="1.5"/>
      <path d="M1 8h14M8 1c3 3 3 11 0 14M8 1c-3 3-3 11 0 14" fill="none" stroke="#4dc08b" stroke-width="1.2"/>
    </svg>
    <span class="site">www.<b>drlucianovarela</b>.com</span>
  </div>
</section>

<section class="card card-back" aria-label="Verso do cartão">
  <div class="icon-tab" aria-hidden="true">
    <svg width="12" height="12" viewBox="0 0 12 12"><path d="M2 1h3l1 3-2 1c1 2 2 3 3 3l1-2 3 1v3c-6 0-9-4-9-9z" fill="#fff"/></svg>
    <svg width="12" height="14" viewBox="0 0 12 14"><rect x="2.5" y="1" width="7" height="12" rx="1.5" fill="#fff"/><rect x="4" y="3" width="4" height="7" fill="#4dc08b"/></svg>
    <svg width="14" height="10" viewBox="0 0 14 10"><rect x="1" y="1" width="12" height="8" fill="#fff"/><path d="M1 1l6 5 6-5" fill="none" stroke="#4dc08b" stroke-width="1.2"/></svg>
  </div>
  <div class="back-content">
    <div class="doctor-name">Dr. Luciano Varela</div>
    <div class="specialty">Cirurgia do Joelho / Esporte</div>
    <p class="contact-line">Centro Executivo - Pinheiral Plaza</p>
    <p class="contact-line">Av. Doutor Augusto Brandão Cunha, 2740 sala 0836</p>
    <p class="contact-line">Jd. Ipanema - Vila Serena - VS</p>
    <p class="contact-line">(10) 3670-4851</p>
    <p class="contact-line">Tel (10) 8245-3908</p>
    <p class="contact-line">drlucianovarela@mailbox-exemplo.com</p>
  </div>
  <div class="back-brand">
    <div class="back-brand-row">
      <span class="brand-square"></span>
      <span class="back-name">VARELA</span>
    </div>
    <div class="back-tagline">Traumatologia Esportiva</div>
  </div>
  <p class="registration"><em>Reg.:</em> CRM 584-902</p>
</section>

</body>
</html>
```